PowerPoint template for Credit Card Processor

We need a powerpoint template for our new credit card processing company. Our goal is to sign up merchants to accept credit cards. We will be making presentations to merchants to get them to sign up for our services.

We already have a logo designed. We'd like to incorporate that logo and color scheme in the powerpoint template. The logo file is an illustrator file.

I generally like light colored backgrounds. Nothing too dark.

Industry/Entity Type

Credit Card

Requirements
Must have
• our logo

```html
<!DOCTYPE html>
<html lang="en">
<head>
<meta charset="utf-8">
<title>ClearSwipe.net — Presentation Template</title>
<link href="https://fonts.googleapis.com/css2?family=Oswald:wght@300;400;600&family=Montserrat:wght@400;600;700&display=swap" rel="stylesheet">
<style>
:root{
  --canvas:#c6c6c6;
  --navy:#1f4f8b;
  --deep:#0d4a7a;
  --mid:#3b8ec8;
  --cyan:#1494cf;
  --sky:#7fd0f5;
  --ink:#4a4a4a;
  --rule:#c9d1d8;
  --white:#ffffff;
  --footer:#555759;
}
*{box-sizing:border-box;margin:0;padding:0}
html,body{width:1060px;height:1200px;overflow:hidden}
body{background:var(--canvas);position:relative;font-family:"Montserrat",sans-serif}
.slide{position:absolute;width:514px;height:385px;overflow:hidden;background:var(--white)}
.col-a{left:12px}.col-b{left:534px}
.row-1{top:9px}.row-2{top:405px}.row-3{top:802px}
.abs{position:absolute}
.brand{display:flex;align-items:center;gap:6px;font-family:"Oswald",sans-serif;font-weight:300;white-space:nowrap;line-height:1}
.brand-dot{border-radius:50%;background:var(--cyan);flex:none}
.condensed{font-family:"Oswald",sans-serif;line-height:1;white-space:nowrap}
.narrow{transform:scaleX(.8);transform-origin:left top}

/* Cover */
.cover{background:var(--navy)}
.cover .brand{left:0;right:0;top:160px;justify-content:center;font-size:52px;color:var(--white);gap:14px}
.cover .brand-dot{width:54px;height:54px;background:#19a8e0}

/* Title — photo */
.title-photo .photo{inset:0;background:linear-gradient(120deg,#0e4a7e 0%,#135f98 38%,#5e9ccb 62%,#1b5f95 82%,#0c4675 100%)}
.title-photo .brand{left:13px;top:76px;font-size:18px;color:var(--white)}
.title-photo .brand-dot{width:14px;height:14px;background:#5cc4f0}
.title-box{left:0;top:123px;width:409px;height:139px;background:var(--mid)}
.title-photo .title{left:17px;top:150px;font-size:50px;font-weight:400;color:var(--white);letter-spacing:.5px}
.title-photo .subtitle{left:18px;top:206px;font-size:25px;font-weight:300;color:var(--sky)}
.meta-company{font-family:"Oswald",sans-serif;font-size:13px;font-weight:400;white-space:nowrap}
.meta-date{font-family:"Oswald",sans-serif;font-size:11px;font-weight:300;white-space:nowrap}
.title-photo .meta-company{left:18px;top:284px;color:var(--white)}
.title-photo .meta-date{left:18px;top:305px;color:var(--sky)}

/* Title — light */
.title-light .photo{inset:0;background:linear-gradient(115deg,#eef1f4 0%,#e6ebf0 45%,#d9e1e8 70%,#eceff3 100%)}
.title-light .brand{left:17px;top:76px;font-size:18px;color:var(--ink)}
.title-light .brand-dot{width:14px;height:14px}
.title-band{left:0;top:125px;width:111px;height:97px;background:var(--cyan)}
.title-light .title{left:118px;top:124px;font-size:52px;font-weight:400;color:var(--ink)}
.title-light .subtitle{left:118px;top:181px;font-size:25px;font-weight:300;color:var(--ink)}
.title-light .meta-company{left:15px;top:266px;color:var(--ink)}
.title-light .meta-date{left:15px;top:287px;color:var(--cyan)}

/* Agenda */
.agenda .side{left:0;top:0;width:114px;height:385px;background:var(--deep)}
.agenda .side-top{left:0;top:0;width:114px;height:64px;background:var(--cyan)}
.agenda .brand{left:13px;top:27px;font-size:11px;color:var(--white);gap:4px}
.agenda .brand-dot{width:9px;height:9px;background:var(--white)}
.side-title{left:0;width:114px;top:355px;text-align:center;color:var(--white);font-size:13px;font-weight:300}
.side-sub{left:0;width:114px;top:371px;text-align:center;color:var(--sky);font-family:"Oswald",sans-serif;font-size:6px;font-weight:300}
.agenda-heading{left:130px;top:52px;font-size:28px;font-weight:600;color:#2f8fcf;letter-spacing:.3px}
.agenda-item{position:absolute;left:130px;width:384px;height:20px}
.agenda-item .topic{position:absolute;left:2px;top:0;font-family:"Oswald",sans-serif;font-weight:300;font-size:14px;color:var(--ink);white-space:nowrap}
.agenda-item .topic::after{content:"";position:absolute;left:-2px;top:22px;width:350px;border-bottom:1px solid var(--rule)}
.agenda-item .page{position:absolute;right:9px;top:4px;font-family:"Montserrat",sans-serif;font-size:10px;color:var(--cyan)}
.agenda-item .page::after{content:"";position:absolute;left:-9px;top:18px;width:26px;border-bottom:1px solid #9cb9d3}

/* Content */
.content-head{left:0;top:0;width:514px;height:48px;background:var(--cyan)}
.content-title{left:8px;top:12px;font-family:"Montserrat",sans-serif;font-size:22px;font-weight:400;color:var(--white);white-space:nowrap;letter-spacing:.2px}
.placeholder{left:24px;top:76px;width:222px;height:257px;background:#3388c4}
.bullets{left:264px;top:97px;width:225px;list-style:none;font-size:7.6px;line-height:1.45;color:var(--ink)}
.bullets li{position:relative;margin-bottom:9px;padding-left:12px;text-align:justify}
.bullets li::before{content:"";position:absolute;left:1px;top:4px;width:7px;height:2.5px;border-radius:2px;background:var(--cyan)}
.bullets li.sub{margin-left:30px}
.bullets li.sub::before{background:#5cc4f0}
.bullets b{font-weight:700}
.footer{left:0;top:363px;width:514px;height:22px;background:var(--footer);display:flex;align-items:center}
.footer .num{width:20px;height:22px;background:var(--cyan);color:var(--white);font-size:9px;display:flex;align-items:center;justify-content:center}
.footer .brand{position:static;font-size:12px;color:var(--white);margin-left:12px;gap:4px}
.footer .brand-dot{width:8px;height:8px;background:var(--white)}
.footer .sep{color:var(--white);font-size:8px;margin-left:7px;white-space:nowrap}
.footer .sub{color:#5cc4f0;font-size:6.5px;margin-left:8px;white-space:nowrap}

/* Closing */
.closing .brand{left:0;right:0;top:163px;justify-content:center;font-size:54px;color:var(--ink);gap:14px}
.closing .brand-dot{width:54px;height:54px;background:#19a8e0}
.contact{left:14px;top:302px;color:var(--ink);font-size:6.5px;line-height:1.35}
.contact h3{font-size:8.5px;font-weight:700;margin-bottom:1px}
.contact .block+.block{margin-top:12px}
.social{top:360px;width:17px;height:17px}
.social-1{left:429px;background:#5ab4e5}
.social-2{left:455px;background:#3b83c5}
.social-3{left:481px;background:#1a6fb0}
</style>
</head>
<body>

<section class="slide cover col-a row-1">
  <div class="brand abs"><span class="brand-dot"></span>ClearSwipe.net</div>
</section>

<section class="slide title-photo col-b row-1">
  <div class="photo abs" role="img" aria-label="Close-up photograph of a credit card chip and embossed numbers in blue tones"></div>
  <div class="brand abs"><span class="brand-dot"></span>ClearSwipe.net</div>
  <div class="title-box abs"></div>
  <div class="title condensed narrow abs">PRESENTATION TITLE</div>
  <div class="subtitle condensed abs">Presentation Subtitle</div>
  <div class="meta-company abs">Company Presentation</div>
  <div class="meta-date abs">September 2013</div>
</section>

<section class="slide title-light col-a row-2">
  <div class="photo abs" role="img" aria-label="Faded light photograph of a credit card surface"></div>
  <div class="brand abs"><span class="brand-dot"></span>ClearSwipe.net</div>
  <div class="title-band abs"></div>
  <div class="title condensed narrow abs">PRESENTATION TITLE</div>
  <div class="subtitle condensed abs">Presentation Subtitle</div>
  <div class="meta-company abs">Company Presentation</div>
  <div class="meta-date abs">September 2013</div>
</section>

<section class="slide agenda col-b row-2">
  <div class="side abs"></div>
  <div class="side-top abs"></div>
  <div class="brand abs"><span class="brand-dot"></span>ClearSwipe.net</div>
  <div class="side-title condensed abs">PRESENTATION TITLE</div>
  <div class="side-sub abs">Presentation Subtitle</div>
  <h2 class="agenda-heading condensed narrow abs">TODAY’S AGENDA</h2>
  <div class="agenda-item" style="top:92px"><span class="topic">Presentation Topic Title</span><span class="page">#</span></div>
  <div class="agenda-item" style="top:139px"><span class="topic">Presentation Topic Title</span><span class="page">#</span></div>
  <div class="agenda-item" style="top:192px"><span class="topic">Presentation Topic Title</span><span class="page">#</span></div>
  <div class="agenda-item" style="top:242px"><span class="topic">Presentation Topic Title</span><span class="page">#</span></div>
  <div class="agenda-item" style="top:300px"><span class="topic">Presentation Topic Title</span><span class="page">#</span></div>
</section>

<section class="slide content col-a row-3">
  <div class="content-head abs"></div>
  <h2 class="content-title abs">PRESENTATION SLIDE TITLE</h2>
  <div class="placeholder abs" role="img" aria-label="Image placeholder">
    <svg width="222" height="257" aria-hidden="true">
      <rect x="74" y="92" width="74" height="74" fill="none" stroke="#4fa3db" stroke-width="4"/>
      <circle cx="100" cy="114" r="7" fill="#4fa3db"/>
      <path d="M84 158 L103 130 L114 144 L124 126 L140 158 Z" fill="#4fa3db"/>
    </svg>
  </div>
  <ul class="bullets abs">
    <li><b>Aenean</b> ridiculus tortor quis interdum id habitant ad, natoque consectetuer nisl auctor libero quisque euismod ante inceptos malesuada ligula mattis.</li>
    <li class="sub">Nulla, netus pulvinar pellentesque porttitor purus maecenas tellus hac nulla lacus. Lorem. Nostra laoreet nulla, dis cursus nascetur dolor odio Eu Magna molestie montes dui mus cursus habitasse mauris tempor.</li>
    <li class="sub">Varius inceptos <b>nascetur</b> mollis dui aptent ultrices. Pretium pulvinar ante lobortis convallis lectus netus vitae penatibus eros at blandit. Parturient.</li>
    <li><b>Aenean</b> ridiculus tortor quis interdum id habitant ad, natoque consectetuer nisl auctor libero quisque euismod ante inceptos malesuada ligula mattis.</li>
  </ul>
  <div class="footer abs">
    <span class="num">5</span>
    <span class="brand"><span class="brand-dot"></span>ClearSwipe.net</span>
    <span class="sep">|&nbsp;&nbsp;PRESENTATION TITLE</span>
    <span class="sub">Presentation Subtitle</span>
  </div>
</section>

<section class="slide closing col-b row-3">
  <div class="brand abs"><span class="brand-dot"></span>ClearSwipe.net</div>
  <div class="contact abs">
    <div class="block">
      <h3>Contact us:</h3>
      <p>555-010-0199</p>
      <p>sales@clearswipe.net</p>
    </div>
    <div class="block">
      <h3>Our Office</h3>
      <p>Address Line 1</p>
      <p>Address Line 2</p>
    </div>
  </div>
  <span class="social social-1 abs" role="img" aria-label="Social network link"></span>
  <span class="social social-2 abs" role="img" aria-label="Social network link"></span>
  <span class="social social-3 abs" role="img" aria-label="Social network link"></span>
</section>

</body>
</html>
```